Dentist logo, business card and website

I have done an amateur job of creating a logo, business card and website. I would like it to look more professional. the current website can be found at www.tobenkarsh.com - I would like the website to be built and run through wix.com. The content on the website is as I would like it but I am open to suggestions.

The logo should be simple, may be best to keep to the letter TK - maybe to look like the V is a reflection of the A? Again, I am open to suggestions (I have attached a couple of images I have used on presentations but I would like the logo that you design to have a 'no fill' background so it can be placed on slides (for presentations etc).

The colour scheme seems wrong for a dentist, perhaps duck egg with black writing would be better? This applies to the business card as well (I have attached a PDF of some I have had made in the past but again they look amateur and colour scheme is wrong. The business cards should be landscape, have the logo in the top right corner, my name and qualifications in the middle, and my website and physical address in the bottom left corner: Glenmorrow Dental Surgery, 41-43 Pellow Crescent, Harrowmere CF22 9RW.

Target Market(s)

30-60 year olds

Industry/Entity Type

Dental

Contact Information for Business Card

Please see brief and uploads.

Logo Text

TK

Number of Pages Required

4 page

Font styles to use
Decorative
Script

Requirements
Must have
• A sophisticated mature feel.
Nice to have
• Simplicity.
Should not have
• Anything too complicated.

```html
<!DOCTYPE html>
<html lang="en">
<head>
<meta charset="utf-8">
<title>Toben Karsh – About Me</title>
<link rel="stylesheet" href="https://fonts.googleapis.com/css2?family=Cinzel:wght@400&family=Noto+Sans:wght@400&display=swap">
<style>
  :root {
    --band: #a3cad2;
    --band-line: #b9d8de;
    --panel: #d2e6ea;
    --footer: #d6e8ec;
    --footer-line: #e6f1f3;
    --ink: #2f3b40;
    --ink-soft: #4a575c;
    --nav-active: #c4dfe4;
    --photo-top: #8fb3bc;
    --photo-mid: #6f8aa6;
    --photo-low: #5e7690;
  }
  * { margin: 0; padding: 0; box-sizing: border-box; }
  html, body { width: 1200px; height: 666px; overflow: hidden; }
  body {
    position: relative;
    background: var(--band);
    font-family: "Noto Sans", "Segoe UI", sans-serif;
    color: var(--ink);
  }
  .site-header {
    position: absolute; left: 0; top: 0; width: 1200px; height: 80px;
    border-bottom: 1px solid var(--band-line);
  }
  .brand { position: absolute; left: 288px; top: 28px; display: flex; align-items: flex-start; gap: 12px; }
  .brand-mark { width: 20px; height: 20px; background: var(--ink); margin-top: 2px; }
  .brand-name {
    font-family: "Cinzel", serif; font-size: 21px; line-height: 22px;
    color: var(--ink); letter-spacing: 0.3px;
  }
  .brand-quals { font-size: 7px; color: var(--ink-soft); margin-top: 3px; margin-left: 8px; }
  .main-nav { position: absolute; top: 36px; left: 0; }
  .main-nav a {
    position: absolute; top: 0; height: 21px; line-height: 21px; white-space: nowrap;
    font-size: 11.5px; color: var(--ink); text-decoration: none;
  }
  .main-nav a.is-active { background: var(--nav-active); padding: 0 10px; }
  .portrait {
    position: absolute; left: 0; top: 86px; width: 292px; height: 580px;
    background: linear-gradient(180deg, var(--photo-top) 0%, var(--photo-mid) 45%, var(--photo-low) 100%);
  }
  .lower-panel {
    position: absolute; left: 292px; top: 363px; width: 908px; height: 262px;
    background: var(--panel);
  }
  .intro, .details {
    position: absolute; width: 765px; font-size: 11.5px; line-height: 21px;
    letter-spacing: 0.15px; color: var(--ink);
  }
  .intro { left: 344px; top: 128px; }
  .details { left: 341px; top: 394px; line-height: 22.5px; }
  .intro p { margin-bottom: 21px; }
  .details p { margin-bottom: 22.5px; }
  .site-footer {
    position: absolute; left: 292px; top: 625px; width: 908px; height: 41px;
    background: var(--footer); border-top: 1px solid var(--footer-line);
  }
  .copyright { position: absolute; right: 117px; top: 16px; font-size: 9px; color: var(--ink-soft); }
  .social { position: absolute; right: 73px; top: 18px; display: flex; gap: 10px; }
  .social span { width: 7px; height: 7px; border-radius: 50%; background: var(--ink-soft); }
</style>
</head>
<body>
  <header class="site-header">
    <div class="brand">
      <div class="brand-mark"></div>
      <div>
        <div class="brand-name">Toben Karsh</div>
        <div class="brand-quals">BDS (Hons) MADF CAS</div>
      </div>
    </div>
    <nav class="main-nav">
      <a href="#" style="left:768px">Home</a>
      <a href="#" class="is-active" style="left:812px">About Me</a>
      <a href="#" style="left:897px">Testimonials</a>
      <a href="#" style="left:981px">Patient Resources</a>
      <a href="#" style="left:1090px">Contact</a>
    </nav>
  </header>

  <div class="portrait" role="img" aria-label="Portrait of the dentist in blue scrubs, arms resting on a desk"></div>

  <section class="intro">
    <p>I qualified from Harlowe University and am listed with the National Dental Register (NDR no. 481726)</p>
    <p>I look after my patients at Glenmorrow Dental Surgery, a modern private practice in Glenmorrow Village, Harrowmere. I take a special interest in gum health and in replacing missing teeth with dental implants.</p>
    <p>I also work as a Clinical Research Fellow and Clinical Lecturer at Avonmere Dental Hospital, University of Avonmere. My research covers study design, gum conditions, bone grafting and problems around implants, the testing of oral care products, tooth wear, sensitive teeth and tooth whitening. I take part in clinical studies that are published in peer reviewed journals, and I help teach and train undergraduates in gum care at the University of Avonmere, as well as giving talks at national meetings.</p>
  </section>

  <div class="lower-panel"></div>

  <section class="details">
    <p>I am an active member of the Society for Periodontal Practice and the Global Implant Forum. I also hold membership of the Allied Dental Faculty of the Chartered Academy of Surgeons and serve as the regional delegate on the committee for the Guild of Dental Implantology.</p>
    <p>I like working closely with my patients to meet their oral health goals, and I know that each person's history and situation are key to understanding what they need. That is why I offer a caring, personal approach shaped to every patient, from the anxious visitor to those hoping to enhance their smile.</p>
    <p>If you would like to learn more about how I might be able to help you, please get in touch.</p>
  </section>

  <footer class="site-footer">
    <div class="copyright">Toben Karsh. Copyright © 2017.&nbsp; All rights reserved.</div>
    <div class="social"><span></span><span></span></div>
  </footer>
</body>
</html>
```